Postcard Design

The business Logo is 'Brambo' it is grass cutting and maintenance. It will offer grass cutting with stripes including edging. Other services include decking/fencing maintenance, lawn treatment and patio/drive cleaning...... prices start from £10 to include front and rear lawns, Regular cuts or a one off tidy. private and commercial. Contracts welcome.
call 01642385106 or 07481926053 for a free quote.
one of the pics that i have sent is the logo (obviously it would need to be tidied up and neater) that is just rough. The other pic is one of pello cards templates but is the one that is the preferred out of all of them. If it could be similar to that with the logo on would be great.
a before (long scruffy grass) and after (neat Lawn) half and half of the postcard would be great.

Target Market(s)

Middle class home owners.

Industry/Entity Type

Business

Requirements
Must have
• The 'Brambo' logo
Nice to have
• we have a lot of junk mail posted in this area and a lot just gets put in the bin so could you make it eye catching.

```html
<!DOCTYPE html>
<html lang="en">
<head>
<meta charset="utf-8">
<title>Brambo Lawn Care and Maintenance – Postcard</title>
<link rel="stylesheet" href="https://fonts.googleapis.com/css2?family=Oswald:wght@200;300;400;500&family=Arimo:wght@400&display=swap">
<style>
  :root {
    --backdrop: #2b2b2b;
    --card-white: #ffffff;
    --ink-dark: #231f20;
    --pill-dark: #2a2629;
    --green-bright: #3cb44b;
    --green-mid: #1f9a3a;
    --green-deep: #0e6b26;
    --green-band: #177a2e;
    --text-light: #ffffff;
    --frame-white: #ffffff;
  }
  * { box-sizing: border-box; margin: 0; padding: 0; }
  html, body {
    width: 777px; height: 1200px; overflow: hidden;
    background: var(--backdrop);
    font-family: "Oswald", "Arial Narrow", sans-serif;
    font-weight: 300;
  }
  .canvas { position: relative; width: 777px; height: 1200px; }

  /* ---------- Front of card ---------- */
  .card-front {
    position: absolute; left: 21px; top: 24px; width: 734px; height: 566px;
    overflow: hidden; background: #3e7d25;
  }
  .hero-garden {
    position: absolute; left: 0; top: 0; width: 734px; height: 203px;
    background: linear-gradient(180deg, #2f5e22 0%, #4f8a2f 45%, #8cc455 70%, #6fae3e 100%);
  }
  .brand-block { position: absolute; left: 16px; top: 46px; }
  .brand-name {
    display: block; font-family: "Oswald", sans-serif; font-weight: 500;
    font-size: 62px; line-height: 1; color: var(--text-light); letter-spacing: 1px;
  }
  .brand-tagline {
    display: block; font-family: "Arimo", Arial, sans-serif; font-size: 13.5px;
    color: var(--text-light); margin-top: 6px;
  }
  .price-ribbon { position: absolute; left: 620px; top: 0; width: 90px; height: 139px; }
  .price-ribbon svg { position: absolute; inset: 0; }
  .price-text {
    position: absolute; left: 0; top: 12px; width: 90px; text-align: center;
    color: var(--text-light); font-size: 10px; line-height: 1.45;
  }
  .price-text .price-amount { display: block; font-size: 24px; font-weight: 500; line-height: 1.05; }

  .service-band {
    position: absolute; left: 0; top: 203px; width: 734px; height: 159px;
    background: linear-gradient(180deg, var(--green-band), #0f5e22 50%, var(--green-band));
    border-top: 2px solid #2a8f3e; border-bottom: 2px solid #2a8f3e;
  }
  .service-photo { position: absolute; top: 14px; width: 231px; height: 133px; border: 3px solid var(--frame-white); }
  .photo-mowing { left: 10px; background: linear-gradient(160deg, #b54a2c 0%, #c9603d 30%, #6ea73c 55%, #4b8a2a 100%); }
  .photo-borders { left: 252px; background: linear-gradient(180deg, #c9dcea 0%, #4f8a36 40%, #2f6a24 75%, #6fb044 100%); }
  .photo-patio { left: 493px; background: linear-gradient(135deg, #c9b28a 0%, #a88a66 45%, #8a4f3a 75%, #6f3a2c 100%); }

  .lower-lawn {
    position: absolute; left: 0; top: 362px; width: 734px; height: 204px;
    background: linear-gradient(90deg, #5e9a38 0%, #86bd54 45%, #a4cf6c 60%, #4f8a2e 80%, #3f7826 100%);
  }
  .quote-pill {
    position: absolute; left: 0; top: 473px; width: 372px; height: 93px;
    background: var(--pill-dark); border-radius: 0 46px 46px 0;
    padding: 10px 22px 0 14px; text-align: center;
  }
  .quote-call { color: var(--text-light); font-size: 19px; line-height: 1.2; letter-spacing: 0.2px; }
  .quote-numbers {
    color: var(--green-bright); font-size: 32px; font-weight: 200;
    line-height: 1.25; letter-spacing: -1px; white-space: nowrap;
  }
  .quote-numbers .or { color: var(--text-light); font-size: 18px; font-weight: 300; letter-spacing: 0; margin: 0 8px; }

  /* ---------- Back of card ---------- */
  .card-back {
    position: absolute; left: 21px; top: 614px; width: 732px; height: 563px;
    background: var(--card-white); overflow: hidden;
  }
  .service-panel {
    position: absolute; left: 19px; top: 19px; width: 327px; height: 441px;
    box-shadow: 0 6px 8px rgba(0,0,0,0.35);
  }
  .before-after {
    position: absolute; left: 0; top: 0; width: 327px; height: 98px;
    background: linear-gradient(90deg, #6f9a3a 0%, #8fb557 45%, #8cc55a 55%, #5fa53b 100%);
  }
  .before-after span {
    position: absolute; top: 82px; color: var(--text-light);
    font-size: 10px; letter-spacing: 1.5px; opacity: 0.85;
  }
  .label-before { left: 63px; }
  .label-after { left: 229px; }
  .services {
    position: absolute; left: 0; top: 98px; width: 327px; height: 309px;
    background: linear-gradient(180deg, var(--green-deep) 0%, var(--green-bright) 45%, var(--green-mid) 80%, var(--green-deep) 100%);
    text-align: center; color: var(--text-light);
  }
  .services-title { font-size: 28px; font-weight: 400; margin-top: 22px; line-height: 1.2; letter-spacing: 0.5px; }
  .services-list { list-style: none; font-size: 17px; line-height: 1.3; margin-top: 4px; }
  .services-list li { margin-top: 5px; }
  .services-list li.tight { margin-top: 0; }
  .services-call { font-size: 17px; margin-top: 22px; line-height: 1.2; }
  .services-numbers { font-size: 26px; font-weight: 300; line-height: 1.25; letter-spacing: -0.6px; white-space: nowrap; }
  .services-numbers .or { font-size: 15px; letter-spacing: 0; margin: 0 4px; }
  .welcome-bar {
    position: absolute; left: 0; top: 407px; width: 327px; height: 34px;
    background: var(--pill-dark); color: var(--text-light);
    text-align: center; font-size: 18px; line-height: 34px;
  }
  .back-brand { position: absolute; left: 358px; top: 38px; }
  .back-brand .brand-name { color: var(--ink-dark); font-size: 58px; }
  .back-brand .brand-tagline { color: var(--ink-dark); font-size: 13px; }
</style>
</head>
<body>
<main class="canvas">

  <section class="card-front">
    <div class="hero-garden" role="img" aria-label="Photo of a striped lawn in front of flowering garden borders"></div>

    <div class="brand-block">
      <span class="brand-name">Brambo</span>
      <span class="brand-tagline">Lawn Care and Maintenance</span>
    </div>

    <div class="price-ribbon">
      <svg width="90" height="139" viewBox="0 0 90 139" aria-hidden="true">
        <path d="M0 0 H90 V139 L45 112 L0 139 Z" fill="#2fa84a" stroke="#ffffff" stroke-width="1.5"/>
      </svg>
      <p class="price-text">
        start from
        <span class="price-amount">£10</span>
        include front and<br>rear lawns,<br>regular cuts or<br>a one off tidy
      </p>
    </div>

    <div class="service-band">
      <div class="service-photo photo-mowing" role="img" aria-label="Photo of a red lawnmower cutting grass"></div>
      <div class="service-photo photo-borders" role="img" aria-label="Photo of a tidy garden with shrubs and a fence"></div>
      <div class="service-photo photo-patio" role="img" aria-label="Photo of a patio being pressure cleaned"></div>
    </div>

    <div class="lower-lawn" role="img" aria-label="Photo of freshly cut lawn"></div>

    <div class="quote-pill">
      <p class="quote-call">CALL TODAY FOR A FREE QUOTE</p>
      <p class="quote-numbers">01642385106<span class="or">OR</span>07481926053</p>
    </div>
  </section>

  <section class="card-back">
    <div class="service-panel">
      <div class="before-after" role="img" aria-label="Photo of long scruffy grass beside a neatly cut lawn">
        <span class="label-before">BEFORE</span>
        <span class="label-after">AFTER</span>
      </div>
      <div class="services">
        <h2 class="services-title">OUR SERVICE</h2>
        <ul class="services-list">
          <li>Lawn cutting including edging, with stripes.</li>
          <li class="tight">One Off or Regular Cuts</li>
          <li>Garden Maintenance and Lawn Treatment</li>
          <li>Hedge Trimming</li>
          <li>Decking/Fence Maintenance</li>
          <li>Patio and Drive Cleaning</li>
        </ul>
        <p class="services-call">CALL TODAY FOR A FREE QUOTE</p>
        <p class="services-numbers">01642385106<span class="or">OR</span>07481926053</p>
      </div>
      <div class="welcome-bar">Private, Commercial and Contracts Welcome</div>
    </div>

    <div class="brand-block back-brand">
      <span class="brand-name">Brambo</span>
      <span class="brand-tagline">Lawn Care and Maintenance</span>
    </div>
  </section>

</main>
</body>
</html>
```